Anzeigengestaltung für Bernstein Ankaufstage in Wien
Zielgruppe
Zweck dieser Anzeige ist:
sowiele Leute wie möglich zu überzeugen, mit Ihrem Bernstein, zu uns in die Ankaufsaktion zu kommen.
Wer wir sind:
Wir sind eine Firma aus Deutschland, die sich auf die Bewertung und den Ankauf von Bernstein (Rohbernstein, Bernsteinschmuck, Kunstobjekte aus Bernstein etc. ) spezialisiert hat.
Wir führen in verschiedenen Städten Aktionen durch, in denen wir Bernstein bewerten und ggf. auch ankaufen.
Zielgruppe:
Alle leser einer Tageszeitung, Alter 50 + überwiegend ältere Damen, und generel Haushalte die Bernstein besitzen
siehe Bsp. Anzeige Wien (Datei upload)
Aufgabenstellung
Anzeigengröße B 198 mm x H 270 mm
Technische Angaben siehe PDF Tageszeitungproduktion (Datei upload)
Wir wollen auf jedenfall eine Anzeige die auch effektreich ist, nicht nur 2-dimensional und platt bleibt, sondern auch verschiedene Tiefen hat. Aber sie soll trotzdem plakativ sein.
Die Anzeige muss Seriös, Auffälig, gut lesbar, edel, frisch,..... AKTION!!
Zielgruppe ansprechen
Direkt erkennbar sein was die Anzeige bezwecken soll
Unser Hauptinteresse liegt auf den gelben ketten, davon haben wir auch 2 Bilder beigefügt.
Das wichtigste Bild ist Bild: "bernstein_2.jpg", dieses sollte schon irgendwo groß auftauchen.
Das soll auf die Anzeige:
- Textteil wie Beispielsdatei.
- AKTION
- Was....Bernstein Ankaufs-Tage in Wien
- Bernstein-Wertschätzung und Ankauf in Wien
- Wann.....vom 03.08.2017-05.08.2017
- Uhrzeit von 10:00 Uhr bis 17:00 Uhr
- Wo.... Hotel Ostara Palais, Lindauer Gasse 14, 1010 Wien, Raum: Salon 3
- Was Kaufen Wir....... Bernsteinschmuck, Bernsteinketten, Bernsteinobjekte, Rohbernsteine ab 10 g,
Bernstein Kunstgegenstände.
- Wir bieten Ihnen eine kostenlose Wertschätzung Ihrer Bernsteinstücke sowie einen
Bar-Ankauf vor Ort.
- Unser Logo
- Unsere Website www.lindwerk-handel.de
- rechts oben in der Anzeige muss das Wort -ANZEIGE- in klein stehen.
Vermerk, Achtung !!! wir kaufen nur unbehandelten Naturbernstein!!!!
siehe Bsp. Anzeige Wien bei (Datei upload)

```html
<!DOCTYPE html>
<html lang="de">
<head>
<meta charset="utf-8">
<title>Aktion Bernstein – Wertschätzung &amp; Ankauf in Wien</title>
<link href="https://fonts.googleapis.com/css2?family=Montserrat:wght@700;800&family=Marcellus&family=Marcellus+SC&family=Crimson+Text:wght@400;600&display=swap" rel="stylesheet">
<style>
:root{
  --amber:#f39a1f;
  --amber-light:#fbb244;
  --amber-deep:#e07a10;
  --cocoa:#4b3d39;
  --cocoa-dark:#372b28;
  --ink:#2b2523;
  --cream:#fff6e6;
  --paper:#ffffff;
  --muted:#8a8280;
}
*{margin:0;padding:0;box-sizing:border-box}
html,body{width:881px;height:1200px;overflow:hidden;background:var(--paper)}
.ad{position:relative;width:881px;height:1200px;background:var(--paper);font-family:"Crimson Text",Georgia,serif;color:var(--ink)}

.amber-band{background:
  radial-gradient(ellipse at 20% 40%,var(--amber-light),transparent 60%),
  radial-gradient(ellipse at 75% 60%,var(--amber-deep),transparent 55%),
  var(--amber)}

/* left column */
.promo{position:absolute;left:0;top:0;width:504px;height:1200px;overflow:hidden}
.promo-top{position:absolute;left:0;top:0;width:504px;height:72px}
.promo-dark{position:absolute;left:0;top:445px;width:504px;height:710px;background:linear-gradient(180deg,#5a4a45,var(--cocoa) 30%,var(--cocoa-dark))}
.promo-bottom{position:absolute;left:0;top:1155px;width:504px;height:45px;display:flex;align-items:center;justify-content:center}
.website{font-family:"Marcellus",serif;font-size:19px;letter-spacing:1.5px;color:var(--cream)}

.kicker{position:absolute;left:46px;top:14px;font-family:"Montserrat",sans-serif;font-weight:800;font-size:48px;letter-spacing:1px;color:var(--paper)}
.title{position:absolute;left:40px;top:72px;font-family:"Montserrat",sans-serif;font-weight:800;font-size:70px;letter-spacing:-1px;color:var(--amber)}
.subtitle{position:absolute;left:0;width:504px;top:160px;text-align:center;font-family:"Marcellus",serif;font-size:33px;line-height:46px;color:var(--ink)}

.necklace-photo{position:absolute;left:6px;top:250px;width:540px;height:295px;border-radius:48% 52% 45% 55%/55% 50% 50% 45%;
  background:radial-gradient(ellipse at 55% 65%,#fdb938,#f08c16 45%,#c9650d 70%,rgba(201,101,13,0) 72%)}

.event{position:absolute;left:0;width:504px;text-align:center}
.date{top:545px;font-family:"Marcellus",serif;font-size:38px;color:var(--amber)}
.hours{top:600px;font-family:"Marcellus",serif;font-size:28px;color:var(--paper)}
.venue{top:650px;font-family:"Marcellus SC",serif;font-size:30px;color:var(--paper)}
.address{top:690px;font-family:"Marcellus",serif;font-size:20px;color:#e9e2de}
.phone{top:733px;font-family:"Marcellus",serif;font-size:31px;letter-spacing:1px;color:var(--paper)}

.rule{position:absolute;left:48px;width:414px;height:1px;background:var(--amber)}
.offer{position:absolute;left:0;width:504px;top:803px;text-align:center;font-family:"Marcellus",serif;font-size:19.5px;line-height:25px;color:var(--paper)}
.offer em{font-style:normal;color:var(--amber)}

.buy{position:absolute;left:56px;top:908px;display:flex;gap:10px;font-family:"Marcellus",serif;font-size:21px;line-height:29px;color:var(--paper)}
.buy ul{list-style:none}
.buy li::before{content:"•";color:var(--amber);margin-right:8px}

.brand{position:absolute;left:0;width:504px;top:1068px;display:flex;flex-direction:column;align-items:center;gap:10px}
.brand-mark{width:38px;height:38px;border-radius:50%;background:radial-gradient(circle at 40% 35%,#ffd36b,var(--amber) 60%,var(--amber-deep))}
.brand-name{font-family:"Marcellus",serif;font-size:22px;letter-spacing:2px;color:var(--paper)}

/* right column */
.article{position:absolute;left:520px;top:0;width:306px;padding-top:38px}
.article h2{font-family:"Marcellus",serif;font-weight:400;font-size:21px;color:var(--ink);margin-bottom:8px}
.article h3{font-family:"Marcellus",serif;font-weight:400;font-size:17px;color:var(--ink);margin:10px 0 6px}
.article p{font-size:12.3px;line-height:15.6px;text-align:justify;hyphens:auto;color:#3a3331}
.article p::first-letter{float:left;font-family:"Marcellus",serif;font-size:36px;line-height:30px;color:var(--amber);margin:1px 3px 0 0}
.article .indented{padding-left:40px}
.article .indented p{text-indent:0}

.jewelry-photo{position:absolute;left:528px;top:1005px;width:290px;height:165px;border-radius:40% 50% 45% 50%/50% 45% 55% 50%;
  background:radial-gradient(ellipse at 50% 50%,#f7a92a,#d9761a 50%,#9a4a1c 68%,rgba(154,74,28,0) 72%)}

.edge{position:absolute;left:840px;top:0;width:41px;height:1200px;box-shadow:-4px 0 8px rgba(0,0,0,.18)}
.label{position:absolute;left:840px;top:0;width:41px;height:125px;background:var(--paper);display:flex;align-items:center;justify-content:center}
.label span{writing-mode:vertical-rl;transform:rotate(180deg);font-family:"Montserrat",sans-serif;font-size:9px;letter-spacing:1.5px;color:var(--muted)}
</style>
</head>
<body>
<main class="ad">
  <section class="promo">
    <div class="promo-top amber-band"></div>
    <div class="kicker">AKTION</div>
    <h1 class="title">BERNSTEIN</h1>
    <p class="subtitle">WERTSCHÄTZUNG<br>&amp; ANKAUF in Wien</p>

    <div class="promo-dark"></div>
    <div class="necklace-photo" role="img" aria-label="Foto einer gelben Bernsteinkette mit großen ovalen Perlen"></div>

    <p class="event date">03.-05. August 2017</p>
    <p class="event hours">jeweils 10-17 Uhr</p>
    <p class="event venue">Hotel Ostara Palais -</p>
    <p class="event address">Salon 3, Lindauer Gasse 14, 1010 Wien</p>
    <p class="event phone">T: +43 660 218 355 90</p>

    <div class="rule" style="top:787px"></div>
    <p class="offer">Wir bieten Ihnen eine <em>KOSTENLOSE<br>WERTSCHÄTZUNG</em> Ihrer Bernsteinstücke<br>sowie einen <em>BAR-ANKAUF VOR ORT</em>.</p>
    <div class="rule" style="top:897px"></div>

    <div class="buy">
      <span>Wir kaufen</span>
      <ul>
        <li>Bernsteinschmuck</li>
        <li>Bernsteinketten</li>
        <li>Rohbernsteine ab 10 g</li>
        <li>Bernstein Kunstgegenstände</li>
      </ul>
    </div>
    <div class="rule" style="top:1037px"></div>

    <div class="brand">
      <span class="brand-mark"></span>
      <span class="brand-name">LINDWERK</span>
    </div>

    <div class="promo-bottom amber-band"><span class="website">www.lindwerk-handel.de</span></div>
  </section>

  <article class="article">
    <h2>Vergessene Schätze</h2>
    <p>Einst als kostbare Fracht entlang der Bernsteinstraße (östliche römische Route) gelangte Bernstein von der Nord- und Ostsee nach Süden in den Mittelmeerraum. Gezeichnet durch kunstvoll gefertigte Gegenstände und allerlei Schmuck rühmt sich das fossile Harz einer langen und vielfältigen Geschichte. Doch diese facettenreiche Geschichte scheint heute für die meisten in Vergessenheit geraten zu sein und klingt bestenfalls noch wie ein Märchen aus der Kindheit. Oft sogar als „langweilig“ oder „aus der Mode gekommen“ gebrandmarkt, wurde der Naturbernstein hier zunehmend von Juwelier-Schaufenstern und Vitrinen verbannt.</p>

    <div class="indented">
      <h3>Ein neues Kapitel</h3>
      <p>Nichtsdestoweniger wird dem Bernstein heute weltweit mehr Wertschätzung gezollt als je zuvor. Seit Neuestem wurde ein neues Kapitel aufgeschlagen. Die Bernsteinstraße, die einst gen Süden ging, führt heute bis nach China im Fernen Osten. Die aktuelle Nachfrage aus Asien hat den Handel mit Bernstein auf ganz neue Weise wiederbelebt und den Preis teilweise beträchtlich ansteigen lassen. Was mitunter in Wiener Haushalten seit Jahrzehnten in Schmuckkästchen verstaubt, wird in China als begehrtes Schmuckstück teuer gehandelt. Dort gilt Bernstein unter anderem als Symbol des Reichtums und wird stolz in der Öffentlichkeit getragen.</p>
    </div>

    <h3>Große Werte</h3>
    <p>Die Wertbestimmung für Bernstein hat sich jedoch gewandelt und abhängig von bestimmten Merkmalen variiert der Preis sehr stark. Der hier sonst sehr übliche cognacfarbene und transparente Bernsteinschmuck ist kaum mehr gefragt und in jeglicher Form behandelter oder gepresster Bernstein findet so gut wie keine Beachtung mehr. Dahingegen dominiert heute vor allem der unbehandelte naturbelassene Honigbernstein den Handel. Gelb bis orangefarbene milchige in Oliven- oder Kugelform gefertigte Ketten sind die absoluten Renner. Antike Bernsteinketten, die durch Verwitterung im Laufe der Jahre unterschiedlich stark rot bis rotbraun gefärbt wurden, sind besonders interessant. Auch sonstige Schmuckstücke, wie etwa Armbänder, Anhänger, Ringe, Broschen und andere Kleingegenstände sind beliebt. Das gilt auch für Schmuckschatullen, Schnitzereien und Kunstgegenstände aus Natur-Bernstein. Zum einen ist natürlich das Alter und der Zustand für den Preis entscheidend, aber auch Dinge wie Farbe, Größe und Marmorierung sind wichtige Faktoren. Sammler bevorzugen überwiegend gut erhaltene und antike Stücke. Es empfiehlt sich in jedem Fall einen geeigneten Fachmann zu Rate zu ziehen.</p>
  </article>

  <div class="jewelry-photo" role="img" aria-label="Foto von Bernsteinschmuck: Armband, Ketten, Brosche und Anhänger"></div>

  <div class="edge amber-band"></div>
  <div class="label"><span>ANZEIGE</span></div>
</main>
</body>
</html>
```